Need a new letterhead

Need a new fresh exciting letterhead. Remove the footer...info is outdated.

Target Market(s)

B2B

Industry/Entity Type

Electrical Power

Colors

Designer to choose colors to be used in the design.

Requirements
Must have
• Red and Blue Corvane Systems Logo
Nice to have
• Powering a cleaner path forward in footer...reorganize the words?

```html
<!DOCTYPE html>
<html lang="en">
<head>
<meta charset="UTF-8">
<title>Corvane Systems Letterhead</title>
<link href="https://fonts.googleapis.com/css2?family=Outfit:wght@300;400;600;700;800&display=swap" rel="stylesheet">
<style>
  :root {
    --backdrop: #b7b7b9;
    --paper: #ffffff;
    --brand-red: #ee1c25;
    --brand-blue: #283583;
    --ink: #333333;
  }
  * { margin: 0; padding: 0; box-sizing: border-box; }
  html, body { width: 1200px; height: 1000px; overflow: hidden; }
  body { background: var(--backdrop); font-family: "Outfit", sans-serif; position: relative; }
  .letterhead {
    position: absolute; left: 294px; top: 104px;
    width: 612px; height: 792px; background: var(--paper); overflow: hidden;
  }
  .bands { position: absolute; left: 0; top: 0; width: 612px; height: 792px; }
  .brand-name {
    position: absolute; left: 42px; top: 72px;
    font-weight: 800; font-size: 27px; color: var(--brand-red);
    letter-spacing: -0.3px; line-height: 1;
  }
  .recipient {
    position: absolute; left: 79px; top: 165px;
    font-size: 8px; font-weight: 700; color: var(--ink);
  }
  .recipient .name { color: var(--brand-red); }
  .contact { position: absolute; right: 85px; top: 627px; list-style: none; }
  .contact-item {
    display: flex; align-items: center; justify-content: flex-end;
    gap: 8px; margin-bottom: 13px;
  }
  .contact-text {
    text-align: right; font-size: 7.5px; line-height: 11px;
    font-weight: 300; color: var(--ink);
  }
  .contact-icon { width: 20px; height: 20px; display: block; }
  .contact-icon.blue { background: var(--brand-blue); }
  .contact-icon.red { background: var(--brand-red); }
  .tagline {
    position: absolute; right: 10px; top: 741px;
    font-size: 17px; font-weight: 600; color: var(--brand-blue); white-space: nowrap;
  }
</style>
</head>
<body>
  <div class="letterhead">
    <svg class="bands" viewBox="0 0 612 792" aria-hidden="true">
      <polygon fill="var(--brand-red)" points="0,0 431,0 458,39 336,39 316,15 0,15"/>
      <polygon fill="var(--brand-blue)" points="456,23 612,23 612,39 466,39"/>
      <polygon fill="var(--brand-blue)" points="0,743 120,743 138,767 612,767 612,792 0,792"/>
      <polygon fill="var(--brand-red)" points="137,743 326,743 340,760 148,760"/>
    </svg>

    <div class="brand-name">Corvane Systems</div>

    <p class="recipient">To: <span class="name">Dana</span></p>

    <ul class="contact">
      <li class="contact-item">
        <p class="contact-text">415 Harbor Crest Road<br>Eastfield, Maryland 21044</p>
        <svg class="contact-icon blue" viewBox="0 0 20 20" aria-hidden="true">
          <path d="M10 4a3.5 3.5 0 0 0-3.5 3.5c0 2.6 3.5 6.5 3.5 6.5s3.5-3.9 3.5-6.5A3.5 3.5 0 0 0 10 4z" fill="none" stroke="#fff" stroke-width="1.2"/>
          <circle cx="10" cy="7.5" r="1.2" fill="#fff"/>
          <ellipse cx="10" cy="15.5" rx="5" ry="1.4" fill="none" stroke="#fff" stroke-width="1"/>
        </svg>
      </li>
      <li class="contact-item">
        <p class="contact-text">Phone: 877-555-0142<br>Fax: 877-555-0143</p>
        <svg class="contact-icon red" viewBox="0 0 20 20" aria-hidden="true">
          <path d="M6.2 4.5l2 2.3-1.2 1.5c.8 1.7 2 2.9 3.7 3.7l1.5-1.2 2.3 2-1.1 2c-4.6-.3-8.2-3.9-8.5-8.5z" fill="#fff"/>
        </svg>
      </li>
      <li class="contact-item">
        <p class="contact-text">CorvaneSystems.com</p>
        <svg class="contact-icon red" viewBox="0 0 20 20" aria-hidden="true">
          <g fill="none" stroke="#fff" stroke-width="1.1">
            <circle cx="10" cy="10" r="5.5"/>
            <ellipse cx="10" cy="10" rx="2.4" ry="5.5"/>
            <line x1="4.5" y1="10" x2="15.5" y2="10"/>
            <line x1="5.3" y1="7.3" x2="14.7" y2="7.3"/>
            <line x1="5.3" y1="12.7" x2="14.7" y2="12.7"/>
          </g>
        </svg>
      </li>
    </ul>

    <p class="tagline">Powering a cleaner path forward</p>
  </div>
</body>
</html>
```